Brindle Works Australia Website

Brindle Works Australia (BWA) is a Industrial, Mining & Transport Services provider in Australia. We require a website that is both pc and mobile freindly. The website will be used to both present our company services and give us exposure in a crowded market. The main page of the website will have a snapshot of who BWA is and its from this page that the user can click to enter the area of interest ie. Industrial, Mining and Transport. A disticted logo can be used to indicate the area in question.<br/>Within the industrial, Mining and the Transport services pages will need list and description of services that are provided, current customer lists and news pages.<br/>The website will need a contacts page so prospective customers can get in contact with BWA.<br/>The website design will require a user freindly back end so future updates and ammendments can be carriedout by less experienced people within the BWA business.

Target Market(s)

Industrial, Mining and Transport Services provider markets

Coding

Coded - Design and coding required

Number of Pages Required

5+ page

Font styles to use
Sans Serif

Colors
00a990

Requirements
Must have
• Ability to build servises with in services. because the main service area is only the main service with in each service group there is alot of smaller services / tasks.
• Key wording for easy seach engine capabilities. The website will need to be search engine freindly.

```html
<!DOCTYPE html>
<html lang="en">
<head>
<meta charset="utf-8">
<title>Brindle Works Australia</title>
<link href="https://fonts.googleapis.com/css2?family=Black+Ops+One&family=Rubik:wght@400;500;600&family=Lato:ital,wght@0,400;0,700;1,400&display=swap" rel="stylesheet">
<style>
:root{
  --green:#248f17;
  --green-dark:#1c7411;
  --ink:#111;
  --text:#333;
  --muted:#9a9a9a;
  --line:#e6e6e6;
  --soft:#f8f8f8;
  --footer:#232323;
  --footer-deep:#171717;
}
*{box-sizing:border-box;margin:0;padding:0}
html,body{width:1200px;height:4521px;overflow:hidden}
body{position:relative;font-family:"Lato",sans-serif;color:var(--text);background:#fff}
.abs{position:absolute}
h2.section-title{font-family:"Rubik",sans-serif;font-weight:500;font-size:36px;color:var(--ink);letter-spacing:.5px;text-transform:uppercase}
h2.section-title span{color:var(--green)}
.btn{display:inline-flex;align-items:center;justify-content:center;background:var(--green);color:#fff;font-family:"Rubik",sans-serif;font-size:15px;text-transform:uppercase;border-radius:3px;width:146px;height:52px}
.body-copy{font-size:13px;line-height:27px;color:var(--muted)}
.photo{position:absolute}

/* top bar */
.topbar{top:0;left:0;width:1200px;height:52px;border-bottom:1px solid var(--line)}
.topbar .social{position:absolute;left:77px;top:0;display:flex;height:52px}
.topbar .social span{width:52px;height:52px;border-left:1px solid var(--line);display:flex;align-items:center;justify-content:center}
.topbar .social span:last-child{border-right:1px solid var(--line)}
.topbar .social i{width:10px;height:10px;border-radius:50%;background:#bbb;display:block}
.topbar .info{position:absolute;top:0;height:52px;display:flex;align-items:center;padding-left:22px;border-left:1px solid var(--line);font-size:12px;color:#777}
.topbar .info b{color:#444;font-weight:700;margin-right:4px}

/* header */
.header{top:52px;left:0;width:1200px;height:104px}
.brand{position:absolute;left:77px;top:26px;display:flex;align-items:center;gap:10px}
.brand i{width:40px;height:40px;background:var(--green);display:block}
.brand span{font-family:"Rubik",sans-serif;font-weight:600;color:var(--green);font-size:19px;line-height:22px;width:140px}
.nav a{position:absolute;top:0;height:104px;line-height:104px;font-family:"Rubik",sans-serif;font-size:14px;color:#999;text-decoration:none;text-transform:uppercase}
.nav a.active{color:var(--green)}
.nav a.active::after{content:"";position:absolute;left:0;right:0;bottom:0;height:4px;background:var(--green)}

/* hero */
.hero{top:156px;left:0;width:1200px;height:572px;background:linear-gradient(180deg,#5a5f66 0%,#4b4a44 45%,#6b4e36 80%,#7a573a 100%)}
.hero .shade{position:absolute;inset:0;background:rgba(0,0,0,.25)}
.hero h1{position:absolute;top:140px;left:0;width:1200px;text-align:center;font-family:"Black Ops One",sans-serif;font-weight:400;color:#fff;font-size:104px;line-height:100px}
.hero h1 small{display:block;font-size:44px;line-height:52px;margin-top:10px}
.hero .btn{position:absolute;left:526px;top:391px;width:146px;height:51px}
.arrow{position:absolute;top:260px;width:53px;height:52px;background:var(--green);display:flex;align-items:center;justify-content:center}

/* about */
.about h2{left:79px;top:790px}
.about .body-copy{left:79px;top:856px;width:470px}
.about .body-copy p+p{margin-top:10px}
.about .btn{left:77px;top:1114px}

/* services */
.services{top:1228px;left:0;width:1200px;height:1491px;background:var(--soft)}
.services .intro{position:absolute;top:132px;left:0;width:1200px;text-align:center;font-style:italic;font-size:15px;line-height:29px;color:#666}
.svc h3{font-family:"Rubik",sans-serif;font-weight:500;font-size:32px;color:var(--ink)}
.svc .body-copy{width:460px;margin-top:18px}
.svc .btn{margin-top:22px}

/* news */
.tabs{left:707px;top:2780px;width:416px;height:53px;border:1px solid var(--line);display:flex;align-items:center;font-family:"Rubik",sans-serif;font-size:15px;color:#555;text-transform:uppercase}
.tabs .on{background:#111;color:#fff;height:53px;width:146px;display:flex;align-items:center;justify-content:center;margin:-1px 0 0 -1px}
.news-item{left:79px;width:365px}
.news-item h4{font-family:"Rubik",sans-serif;font-weight:500;font-size:14px;line-height:23px;color:#111}
.news-item time{display:block;margin-top:10px;font-size:12px;color:var(--green);font-weight:700}
.divider{left:77px;width:365px;height:1px;background:var(--line)}
.card{left:519px;top:2884px;width:604px;height:405px;background:var(--soft);border:1px solid #eee}
.card .meta{position:absolute;left:293px;top:56px;display:flex;align-items:center;gap:26px;font-size:12px;font-weight:700;color:#222}
.card .tag{background:var(--green);color:#fff;font-weight:400;font-size:11px;padding:7px 14px}
.card h4{position:absolute;left:293px;top:120px;width:290px;font-family:"Rubik",sans-serif;font-weight:500;font-size:16px;line-height:26px;color:#111}
.card .body-copy{position:absolute;left:293px;top:210px;width:290px;font-size:12.5px;line-height:27px}
.card .by{position:absolute;left:293px;top:336px;font-size:12px;color:#555}
.card .by b{color:#222}

/* cta */
.cta{top:3350px;left:0;width:1200px;height:293px;background:linear-gradient(90deg,#2f8f1a,#3e9a22 50%,#2f8a16)}
.cta p{position:absolute;top:58px;left:0;width:1200px;text-align:center;color:#fff;font-family:"Rubik",sans-serif;font-size:33px;line-height:47px}
.cta .ghost{position:absolute;left:500px;top:179px;width:200px;height:51px;border:1px solid #fff;border-radius:4px;color:#fff;font-family:"Rubik",sans-serif;font-size:15px;display:flex;align-items:center;justify-content:center}

/* contact */
.contact h2{left:79px;top:3705px}
.contact .lead{left:79px;top:3776px;width:420px;font-style:italic;font-size:15px;line-height:29px;color:#666}
.c-row{left:77px;display:flex;align-items:center;gap:24px;font-family:"Rubik",sans-serif;font-size:18px;color:#222}
.c-row .ic{width:52px;height:52px;border:3px solid #c8e2c3;border-radius:4px;display:flex;align-items:center;justify-content:center;background:var(--green);background-clip:content-box}
.c-row.addr{font-size:15px;line-height:27px;color:#666}
.form{left:623px;top:3706px;width:500px;height:376px;background:#fff;box-shadow:0 0 14px rgba(0,0,0,.1)}
.field{position:absolute;border-bottom:1px solid #ddd;font-size:12px;color:#888;padding-bottom:20px}
.form .send{position:absolute;left:44px;top:271px;width:416px;height:51px;background:var(--green);color:#fff;font-family:"Rubik",sans-serif;font-size:15px;display:flex;align-items:center;justify-content:center;border-radius:3px}

/* footer */
.footer{top:4143px;left:0;width:1200px;height:289px;background:var(--footer)}
.footer .brand{left:0;width:1200px;justify-content:center;top:68px}
.footer .links{position:absolute;top:157px;width:1200px;text-align:center;font-size:14px;color:#bbb}
.footer .links span{margin:0 8px;color:#777}
.footer .soc{position:absolute;top:200px;left:0;width:1200px;display:flex;justify-content:center;gap:7px}
.footer .soc i{width:46px;height:46px;border-radius:50%;background:#3d3d3d;display:block}
.copy{top:4432px;left:0;width:1200px;height:89px;background:var(--footer-deep);color:#4a4a4a;font-size:12px;text-align:center;line-height:89px}
</style>
</head>
<body>

<div class="abs topbar">
  <div class="social"><span><i></i></span><span><i></i></span><span><i></i></span><span><i></i></span></div>
  <div class="info" style="left:721px;width:193px"><b>PHONE :</b>123.456.7890</div>
  <div class="info" style="left:914px;width:209px;border-right:1px solid var(--line)"><b>EMAIL :</b>infobwaservices.com</div>
</div>

<header class="abs header">
  <div class="brand"><i></i><span>Brindle Works Australia</span></div>
  <nav class="nav">
    <a class="active" style="left:549px">Home</a>
    <a style="left:632px">About</a>
    <a style="left:720px">Services</a>
    <a style="left:825px">Clients</a>
    <a style="left:918px">News</a>
    <a style="left:997px">Contact</a>
  </nav>
  <svg class="abs" style="left:1102px;top:42px" width="22" height="22" viewBox="0 0 22 22" fill="none" stroke="#333" stroke-width="2"><circle cx="9" cy="9" r="7"/><path d="M14 14l6 6"/></svg>
</header>

<section class="abs hero" role="img" aria-label="Large haul truck and excavator at an open-cut mine">
  <div class="shade"></div>
  <h1>BWA<small>MINING AND TRANSPORT<br>SERVICES</small></h1>
  <span class="btn">Contact Us</span>
  <div class="arrow" style="left:51px"><svg width="12" height="16" viewBox="0 0 12 16" fill="none" stroke="#fff" stroke-width="2"><path d="M8 2L2 8l6 6"/></svg></div>
  <div class="arrow" style="left:1096px"><svg width="12" height="16" viewBox="0 0 12 16" fill="none" stroke="#fff" stroke-width="2"><path d="M4 2l6 6-6 6"/></svg></div>
</section>

<section class="about">
  <h2 class="abs section-title">About <span>BWA</span></h2>
  <div class="abs body-copy">
    <p>Lorem ipsum dolor sit amet, consectetur adipiscing elit, sed do eiusmod tempor incididunt ut labore et dolore magna aliqua. Ut enim ad minime veniam, quis nostrud exercitation ullamco laboris nisi ut aliquip ex eax commodo consequat. Duis aute irure dolor in reprehenderit ivoluptate velit esse cillum dolore eu fugiat nulla pariatur.</p>
    <p>Lorem ipsum dolor sit amet, consectetur adipiscing elit, sed do eiusmod tempor incididunt ut labore et dolore magna aliqua. Ut enim ad minime veniam, quis nostrud exercitation ullamco laboris.</p>
  </div>
  <span class="abs btn">Lean More</span>
  <div class="photo" style="left:852px;top:791px;width:271px;height:374px;background:linear-gradient(160deg,#2f9a1c,#1f7d12)"></div>
  <div class="photo" role="img" aria-label="White container truck carrying a blue shipping container" style="left:622px;top:855px;width:340px;height:245px;background:radial-gradient(ellipse at 55% 50%,#8ea0c4 0%,#5f78ad 40%,rgba(230,230,230,.0) 72%)"></div>
</section>

<section class="abs services">
  <h2 class="section-title" style="position:absolute;top:62px;left:0;width:1200px;text-align:center">Our <span>Services</span></h2>
  <p class="intro">Lorem ipsum dolor sit amet, consectetur adipiscing elit, sed do eiusmod tempor<br>incididunt ut labore et dolore magna aliqua.</p>
</section>

<div class="photo" role="img" aria-label="Industrial power plant with cooling towers" style="left:77px;top:1468px;width:523px;height:416px;background:linear-gradient(180deg,#c9d3de 0%,#a9b3b8 45%,#8a8c80 75%,#6f7365 100%)"></div>
<div class="abs svc" style="left:656px;top:1538px">
  <h3>BWA Industrial Services</h3>
  <p class="body-copy">Lorem ipsum dolor sit amet, consectetur adipiscing elit, sed do eiusmod tempor incididunt ut labore et dolore magna aliqua. Ut enim ad minime veniam, quis nostrud exercitation ullamco laboris nisi ut aliquip ex eax commodo consequat. Duis aute irure dolor in reprehenderit ivoluptate velit esse cillum dolore eu fugiat nulla pariatur.</p>
  <span class="btn">Lean More</span>
</div>

<div class="abs svc" style="left:79px;top:1954px">
  <h3>BWA Mining Services</h3>
  <p class="body-copy">Lorem ipsum dolor sit amet, consectetur adipiscing elit, sed do eiusmod tempor incididunt ut labore et dolore magna aliqua. Ut enim ad minime veniam, quis nostrud exercitation ullamco laboris nisi ut aliquip ex eax commodo consequat. Duis aute irure dolor in reprehenderit ivoluptate velit esse cillum dolore eu fugiat nulla pariatur.</p>
  <span class="btn">Lean More</span>
</div>
<div class="photo" role="img" aria-label="Mobile crane beside steel structures on a work site" style="left:600px;top:1884px;width:523px;height:416px;background:linear-gradient(180deg,#b9bcbd 0%,#a3a29c 50%,#9a8b70 80%,#8d7a5d 100%)"></div>

<div class="photo" role="img" aria-label="Truck hauling a shipping container in a port yard" style="left:77px;top:2300px;width:523px;height:417px;background:linear-gradient(180deg,#7fa6d6 0%,#b8cbe0 40%,#9aa0a3 70%,#a7a79f 100%)"></div>
<div class="abs svc" style="left:656px;top:2370px">
  <h3>BWA Transport</h3>
  <p class="body-copy">Lorem ipsum dolor sit amet, consectetur adipiscing elit, sed do eiusmod tempor incididunt ut labore et dolore magna aliqua. Ut enim ad minime veniam, quis nostrud exercitation ullamco laboris nisi ut aliquip ex eax commodo consequat. Duis aute irure dolor in reprehenderit ivoluptate velit esse cillum dolore eu fugiat nulla pariatur.</p>
  <span class="btn">Lean More</span>
</div>

<section class="news">
  <h2 class="abs section-title" style="left:79px;top:2780px">News <span>Feed</span></h2>
  <div class="abs tabs"><span class="on">Industrial</span><span style="margin-left:30px">Mining</span><span style="margin:0 26px;color:#999">|</span><span>Transport</span></div>

  <div class="abs news-item" style="top:2884px"><h4>Lorem ipsum dolor sit amet, consectetur adipiscing elit, sed do eiusmod tempor incididunt.</h4><time>Jan 06 , 2020</time></div>
  <div class="abs divider" style="top:2987px"></div>
  <div class="abs news-item" style="top:3009px"><h4>Lorem ipsum dolor sit amet, consectetur adipiscing elit, sed do eiusmod tempor incididunt.</h4><time>Jan 06 , 2020</time></div>
  <div class="abs divider" style="top:3112px"></div>
  <div class="abs news-item" style="top:3134px"><h4>Lorem ipsum dolor sit amet, consectetur adipiscing elit, sed do eiusmod tempor incididunt.</h4><time>Jan 06 , 2020</time></div>
  <span class="abs btn" style="left:77px;top:3238px;height:51px">Lean More</span>

  <article class="abs card">
    <div class="photo" role="img" aria-label="Two workers reviewing paperwork beside a truck cab" style="left:0;top:0;width:260px;height:403px;background:linear-gradient(180deg,#d9dcdf 0%,#9aa3ad 45%,#5a6676 75%,#3e4550 100%)"></div>
    <div class="meta"><span>Jan 06 , 2020</span><span class="tag">INDUSTRIAL</span></div>
    <h4>Lorem ipsum dolor sit consectetur adipiscing elit, sed do eiusmod dolore magna aliqua.</h4>
    <p class="body-copy">Lorem ipsum dolor sit amet, consectetur to adipiscing elit, sed do eiusmod tempor the incididunt ut labore et dolore magnaliqua. Ut enim ad minime veniam,</p>
    <p class="by">By <b>ADMIN</b> &nbsp; | &nbsp; <b>10 Comments</b></p>
  </article>
</section>

<section class="abs cta" role="img" aria-label="Green tinted highway with trucks">
  <p>Get Free Inquiry of for further information<br>Please Call Us at 123.456.7890</p>
  <span class="ghost">GET A FREE QUOTE</span>
</section>

<section class="contact">
  <h2 class="abs section-title">Contact <span>Us</span></h2>
  <p class="abs lead">Lorem ipsum dolor sit amet, consectetur adipiscing elit, sed do eiusmod tempor incididunt ut labore.</p>
  <div class="abs c-row" style="top:3862px"><span class="ic"><svg width="18" height="14" viewBox="0 0 18 14" fill="none" stroke="#fff" stroke-width="1.6"><rect x="1" y="1" width="16" height="12"/><path d="M1 1l8 7 8-7"/></svg></span>123.456.7890</div>
  <div class="abs c-row" style="top:3945px"><span class="ic"><svg width="16" height="16" viewBox="0 0 24 24" fill="#fff"><path d="M6.6 10.8a15.1 15.1 0 006.6 6.6l2.2-2.2a1 1 0 011-.25 11.4 11.4 0 003.6.57 1 1 0 011 1V20a1 1 0 01-1 1A17 17 0 013 4a1 1 0 011-1h3.5a1 1 0 011 1 11.4 11.4 0 00.57 3.6 1 1 0 01-.25 1z"/></svg></span>infobwaservices.com</div>
  <div class="abs c-row addr" style="top:4028px"><span class="ic"><svg width="14" height="18" viewBox="0 0 14 18" fill="#fff"><path d="M7 0a7 7 0 00-7 7c0 5 7 11 7 11s7-6 7-11a7 7 0 00-7-7zm0 9.5A2.5 2.5 0 117 4.5a2.5 2.5 0 010 5z"/></svg></span><span>123, Address, State Name, Street,<br>City, Zipcode</span></div>

  <form class="abs form">
    <div class="field" style="left:44px;top:60px;width:186px;border-color:#555">|</div>
    <div class="field" style="left:274px;top:60px;width:186px">Last Name</div>
    <div class="field" style="left:44px;top:122px;width:186px">Email</div>
    <div class="field" style="left:274px;top:122px;width:186px">Phone</div>
    <div class="field" style="left:44px;top:184px;width:416px;padding-bottom:48px">Your Meaasge?</div>
    <span class="send">SEND YOUR MESSAGE</span>
  </form>
</section>

<footer class="abs footer">
  <div class="brand"><i></i><span>Brindle Works Australia</span></div>
  <div class="links">Home<span>|</span>About<span>|</span>Services<span>|</span>Clients<span>|</span>News<span>|</span>Contact</div>
  <div class="soc"><i></i><i></i><i></i><i></i></div>
</footer>
<div class="abs copy">Copyright © BWA MINING &amp; TRANSPORT SERVICES - 2019 .All Right Reserved.</div>

</body>
</html>
```